Eco friendly Swedish beauty products sold in aluminum bottles - label design needed

We need help in designing a series of stick on labels for 80 ml (2.7 fl. oz.) aluminum bottles containing beauty products such as soaps, shampoo etc. The diameter of the bottle is 36 mm and the body of the bottles measures approx. 106 mm.
It is important for us that the label has a simplistic and clean feel with few colors (and the right ones!) and that the label helps amplify this product being both better and a more sustainable alternative to many of our plastic bottle competitors. The design and label should communicate the feel of an Eco-friendly, sustainable and modern brand of high quality - and with a Swedish concept.
We are using Montserrat font in our materials. Find attached information of preferred colors, the bottles and one example of our logotype. I am also available on e-mail should further information be needed.

Looking forward and very excited to receive your suggestions.
Note that we are expecting to start selling a series of approximately 10 different products where I will need one "master design" and then only smaller changes for each of the different products.

Target Market(s)

People whom are aware and not only look at price tag. Private and commercial market.

Industry/Entity Type

Beauty

Font styles to use
Other font styles liked:
• Montserrat

Requirements
Must have
• It must give the feel of being both better and a more sustainable alternative to many of our plastic bottle competitors.
Nice to have
• Simplistic. Clean. Clear.
Should not have
• Wrong colors, too complex designs.

```html
<!DOCTYPE html>
<html lang="en">
<head>
<meta charset="utf-8">
<title>Fjella Skin – Hair Shampoo label series</title>
<link href="https://fonts.googleapis.com/css2?family=Montserrat:wght@300&family=Oswald:wght@500&display=swap" rel="stylesheet">
<style>
  :root {
    --paper: #ffffff;
    --ink: #000000;
    --moss: #8a915a;
    --moss-dark: #6d7433;
    --moss-text: #d9dac4;
    --on-dark: #ffffff;
  }
  html, body {
    margin: 0;
    padding: 0;
    overflow: hidden;
    background: var(--paper);
  }
  .canvas {
    position: relative;
    width: 1200px;
    height: 1200px;
    background: var(--paper);
    overflow: hidden;
  }
  .label {
    position: absolute;
    top: 340px;
    width: 200px;
    height: 700px;
  }
  .label--black { left: 120px; --band: var(--ink); --title: var(--ink); --brand: var(--on-dark); --volume: var(--ink); }
  .label--green { left: 444px; --band: var(--moss); --title: var(--moss-dark); --brand: var(--moss-text); --volume: var(--moss); }
  .label--green-alt { left: 835px; --band: var(--moss); --title: var(--moss-dark); --brand: var(--moss-text); --volume: var(--moss); }

  .product-name {
    position: absolute;
    top: 0;
    left: 16px;
    width: 200px;
    margin: 0;
    font-family: "Oswald", "Arial Narrow", sans-serif;
    font-weight: 500;
    font-size: 25px;
    letter-spacing: 4.4px;
    line-height: 34px;
    color: var(--title);
    white-space: nowrap;
  }
  .band {
    position: absolute;
    top: 44px;
    left: 32px;
    width: 167px;
    height: 655px;
  }
  .band path { fill: var(--band); }

  .brand {
    position: absolute;
    top: 78px;
    left: 138px;
    margin: 0;
    writing-mode: vertical-rl;
    font-family: "Montserrat", Arial, sans-serif;
    font-weight: 300;
    font-size: 42px;
    line-height: 42px;
    letter-spacing: 3px;
    color: var(--brand);
    white-space: nowrap;
  }
  .volume {
    position: absolute;
    top: 627px;
    left: 0;
    writing-mode: vertical-rl;
    transform: rotate(180deg);
    font-family: "Montserrat", Arial, sans-serif;
    font-weight: 300;
    font-size: 17px;
    line-height: 20px;
    color: var(--volume);
    white-space: nowrap;
  }
</style>
</head>
<body>
  <main class="canvas">
    <section class="label label--black">
      <h2 class="product-name">Hair Shampoo</h2>
      <svg class="band" viewBox="0 0 167 655" aria-hidden="true">
        <path d="M0 0 H167 V546 A108 108 0 0 1 0 636.5 Z"/>
      </svg>
      <p class="brand">FJELLA SKIN</p>
      <span class="volume">80 ml</span>
    </section>

    <section class="label label--green">
      <h2 class="product-name">Hair Shampoo</h2>
      <svg class="band" viewBox="0 0 167 655" aria-hidden="true">
        <path d="M0 0 H167 V546 A108 108 0 0 1 0 636.5 Z"/>
      </svg>
      <p class="brand">FJELLA SKIN</p>
      <span class="volume">80 ml</span>
    </section>

    <section class="label label--green-alt">
      <h2 class="product-name">Hair Shampoo</h2>
      <svg class="band" viewBox="0 0 167 655" aria-hidden="true">
        <path d="M0 0 H167 V546 A108 108 0 0 1 0 636.5 Z"/>
      </svg>
      <p class="brand">FJELLA SKIN</p>
      <span class="volume">80 ml</span>
    </section>
  </main>
</body>
</html>
```